Bright Harbor website redesign

We need a redesign for a website: mybrightharbor.com.

I already created a video going over what exactly is needed in the design.

See Video here: https://files.vortexa-share.com/file/d/7kPqLm2Xz9RtYw4Nb8Vc3Hd5Jf6Gs1Aa0/view?usp=sharing

Vortexa Deck shown in Video: https://decks.vortexa-share.com/presentation/d/9QwErTy7UiOpAsDfGhJkLzXcVbNm2Qw3ErTy4UiOpAs/edit?usp=sharing
Updates

Holidays in India so we did not get enough design entries or quality.

Target Market(s)

Dentistry

Industry/Entity Type

Dentistry

Number of Pages Required

1 page

Colors
0094D4
00A9DD
6FCCEA
C7EBF8
E9F6FB
00AB8E
00BBA5
67D7C9
C6EFE9
E9F9F6

Requirements
Must have
• See 13 min video link in description - shows what to do.

```html
<!DOCTYPE html>
<html lang="en">
<head>
<meta charset="utf-8">
<title>Bright Harbor – Dental Care</title>
<link href="https://fonts.googleapis.com/css2?family=Gilda+Display&family=Poppins:wght@300;400;500;600&display=swap" rel="stylesheet">
<style>
:root{
  --navy:#10222c;
  --card:#132631;
  --card-line:#27404d;
  --teal:#00AB8E;
  --teal-2:#00BBA5;
  --teal-soft:#67D7C9;
  --blue:#0094D4;
  --blue-2:#00A9DD;
  --blue-soft:#6FCCEA;
  --white:#ffffff;
  --text-dark:#4a4f55;
  --line:#dfe9ee;
  --star:#f7c531;
}
*{margin:0;padding:0;box-sizing:border-box}
html,body{width:1200px;height:3630px;overflow:hidden}
body{background:var(--navy);font-family:"Poppins",sans-serif;color:var(--white);position:relative}
.serif{font-family:"Gilda Display",serif}
section,header,footer{position:absolute;left:0;width:1200px}
.abs{position:absolute}
.center{text-align:center;left:0;width:1200px}

/* hero */
.hero{top:0;height:712px;background:radial-gradient(ellipse at 50% 40%,#1b3441 0%,#0e1f28 75%)}
.brand{left:60px;top:20px}
.brand-name{font-weight:500;font-size:21px;color:var(--teal-2);display:flex;align-items:center;gap:8px}
.brand-name i{width:9px;height:9px;border-radius:50%;background:var(--blue-2);display:inline-block}
.brand-phone{font-size:13px;font-weight:600;color:var(--blue-2);margin-top:5px;margin-left:8px}
.nav{left:262px;top:30px;display:flex;gap:15px;font-size:11px;align-items:center;color:#e8eef2;white-space:nowrap}
.btn{display:inline-block;border-radius:5px;font-family:"Gilda Display",serif;color:#fff;text-align:center}
.btn-teal{background:var(--teal)}
.btn-blue{background:var(--blue-2)}
.nav-btn{top:19px;height:36px;line-height:36px;font-size:15px}
.hero-title{top:162px;font-size:50px;font-weight:600;letter-spacing:.5px}
.hero-sub{top:228px;font-size:14.5px;color:var(--teal-soft)}
.hero-cta{left:487px;top:272px;width:225px;height:40px;line-height:40px;font-size:18px}
.hero-art{left:350px;top:340px;width:500px;height:260px;border-radius:14px;background:radial-gradient(ellipse at 50% 35%,rgba(226,120,138,.55) 0%,rgba(240,220,210,.35) 45%,rgba(16,34,44,0) 75%)}
.arrow-box{width:38px;height:38px;border:1px solid var(--blue-2);border-radius:6px;top:356px}

/* team */
.team{top:712px;height:435px;background:var(--navy)}
.team-band{left:0;top:0;width:450px;height:66px;background:var(--teal);clip-path:polygon(0 0,100% 0,88% 100%,0 100%)}
.team-band span{position:absolute;left:126px;top:14px;font-size:30px}
.member{top:121px;width:260px;text-align:center}
.member .photo{width:150px;height:170px;margin:0 auto;background:linear-gradient(160deg,#5f6a70,#b9c3c8 60%,#e6ecef)}
.member h3{font-size:17px;color:var(--teal-2);font-weight:400;margin-top:24px}
.member p{font-size:11px;color:var(--blue-2);margin-top:4px}

/* services */
.services{top:1147px;height:600px;background:#fff}
.svc-photo{left:0;top:0;width:600px;height:600px;background:linear-gradient(135deg,#C7EBF8 0%,#e9ded2 45%,#f3ede6 70%,#C6EFE9 100%)}
.svc-title{left:661px;top:70px;font-size:31px;color:var(--teal)}
.svc-text{left:661px;top:120px;width:420px;font-size:11.5px;line-height:20px;color:var(--text-dark)}
.svc-item{height:44px;border:1px solid var(--line);border-radius:5px;display:flex;align-items:center;font-size:13.5px;color:#33383d;width:232px}
.svc-item.active{border-color:var(--teal)}
.svc-icon{width:36px;height:36px;border-radius:5px;margin:0 12px 0 4px;background:linear-gradient(135deg,var(--blue),var(--teal));display:flex;align-items:center;justify-content:center}

/* testimonials */
.reviews{top:1747px;height:598px;background:var(--navy)}
.rv-title{top:64px;font-size:29px;color:var(--teal-2)}
.rv-avg{top:116px;font-size:13px;color:var(--blue-2)}
.rv-stars{left:505px;top:146px;display:flex;gap:6px;align-items:center}
.rv-score{font-size:17px;font-weight:600;margin-left:8px}
.rv-count{left:538px;top:196px;display:flex;align-items:center;gap:8px;font-size:13px}
.rv-card{top:270px;width:307px;height:253px;border:1px solid var(--card-line);border-radius:10px;background:var(--card)}
.rv-avatar{position:absolute;left:22px;top:26px;width:58px;height:58px;border-radius:50%;background:linear-gradient(135deg,#7d8c94,#34505e)}
.rv-name{position:absolute;left:96px;top:30px;font-family:"Gilda Display",serif;font-size:16px;color:var(--blue-2)}
.rv-card .stars{position:absolute;left:96px;top:54px;display:flex;gap:4px}
.rv-body{position:absolute;left:26px;top:110px;width:260px;font-size:11px;line-height:19.5px;color:#dfe6ea}
.rv-date{position:absolute;left:26px;top:215px;font-size:11px;color:#c4ced4}
.rv-src{position:absolute;right:22px;top:210px;font-size:15px;font-weight:600;color:#fff}
.chev{top:398px}

/* difference */
.difference{top:2345px;height:638px;background:#fff}
.diff-title{left:62px;top:74px;font-size:33px;line-height:41px;color:var(--teal)}
.diff-body{left:62px;top:172px;width:470px;font-size:11px;line-height:21px;color:var(--text-dark)}
.diff-body p{margin-bottom:10px}
.diff-link{left:62px;top:530px;font-family:"Gilda Display",serif;font-size:15px;color:var(--text-dark);text-decoration:underline}
.diff-link span{color:var(--teal)}
.diff-photo{left:600px;top:0;width:600px;height:638px;background:linear-gradient(150deg,#6c5a4e 0%,#c4a590 35%,#efdfd3 60%,#C7EBF8 100%)}

/* cta */
.cta{top:2983px;height:300px;background:linear-gradient(100deg,var(--blue) 0%,var(--blue-2) 35%,var(--teal-2) 70%,var(--teal) 100%)}
.cta-title{top:66px;font-size:29px;line-height:38px}
.cta-sub{top:150px;font-size:13px}
.cta-btn{left:487px;top:195px;width:225px;height:41px;line-height:39px;border:1.5px solid #fff;border-radius:5px;font-size:18px;text-align:center;color:#fff}

/* footer */
.footer{top:3283px;height:347px;background:var(--navy)}
.f-brand{left:78px;top:98px;font-size:26px;color:var(--teal-2);font-weight:500}
.f-btn{left:62px;top:169px;width:232px;height:37px;line-height:37px;font-size:15px}
.f-head{top:52px;font-family:"Gilda Display",serif;font-size:16px;color:var(--teal-2)}
.f-row{display:flex;gap:14px;font-size:11px;line-height:19px;color:#e3e9ed;margin-bottom:10px}
.f-hours{font-size:11px;line-height:26px;color:#e3e9ed}
.socials{left:338px;top:224px;display:flex;gap:8px}
.socials i{width:30px;height:30px;border:1.5px solid var(--teal);border-radius:50%}
.map{left:888px;top:90px;width:250px;height:118px;background:linear-gradient(135deg,#eef3f5,#dde7eb);border-radius:2px}
.f-links{left:888px;top:228px;width:260px;font-size:10.5px;line-height:19px;color:#e3e9ed}
.copy{top:3600px;font-size:11px;color:#d8e0e5}
.copy span{color:var(--teal-2)}
</style>
</head>
<body>

<header class="hero">
  <div class="abs brand">
    <div class="brand-name"><i></i>Bright Harbor</div>
    <div class="brand-phone">(714) 555-0182</div>
  </div>
  <nav class="abs nav">
    <svg width="13" height="12" viewBox="0 0 13 12"><path d="M6.5 0L0 6h2v6h3.5V8h2v4H11V6h2z" fill="#00BBA5"/></svg>
    <span>About Us</span><span>Services ▾</span><span>Financing</span><span>Testimonials</span><span>New Patient Visit</span><span>Specials ▾</span><span>Contact Us</span><span>Blog</span>
  </nav>
  <a class="abs btn btn-teal nav-btn" style="left:900px;width:128px">Schedule Online</a>
  <a class="abs btn btn-blue nav-btn" style="left:1035px;width:105px">Emergency</a>

  <h1 class="abs center hero-title">Creating Healthier Smiles</h1>
  <p class="abs center hero-sub">With Advanced Technology and Affordable Treatment</p>
  <a class="abs btn btn-teal hero-cta">Book An Appointment</a>
  <div class="abs hero-art" role="img" aria-label="Photo of a full denture set in front of a dimmed patient portrait"></div>
  <div class="abs arrow-box" style="left:60px"><svg width="38" height="38"><path d="M21 13l-6 6 6 6" stroke="#00A9DD" fill="none" stroke-width="1.5"/></svg></div>
  <div class="abs arrow-box" style="left:1100px"><svg width="38" height="38"><path d="M17 13l6 6-6 6" stroke="#00A9DD" fill="none" stroke-width="1.5"/></svg></div>
</header>

<section class="team">
  <div class="abs team-band"><span class="serif">Meet Our Team</span></div>
  <div class="abs member" style="left:208px">
    <div class="photo" role="img" aria-label="Portrait of a cosmetic dentist in a white coat"></div>
    <h3 class="serif">Meet Dr. Priya Nair</h3><p>Cosmetic Dentist</p>
  </div>
  <div class="abs member" style="left:470px;top:125px">
    <div class="photo" role="img" aria-label="Portrait of an endodontist in a dark blazer"></div>
    <h3 class="serif">Meet Dr. Anika Rao</h3><p>Endodontist</p>
  </div>
  <div class="abs member" style="left:730px">
    <div class="photo" role="img" aria-label="Portrait of a general dentist in a white coat"></div>
    <h3 class="serif">Meet Dr. Vikram Desai</h3><p>General Dentist</p>
  </div>
</section>

<section class="services">
  <div class="abs svc-photo" role="img" aria-label="Smiling patient holding a hand mirror while a dentist checks tooth shade"></div>
  <h2 class="abs svc-title serif">Our Services</h2>
  <p class="abs svc-text">We Value our Client's Smile. We know how Important it is for you to Have your Confidence Back.</p>
  <svg width="0" height="0" style="position:absolute"><defs><path id="tooth" d="M4 3c2-1 4 0 6 0s4-1 6 0c2 2 1 6-1 8l-1 7h-2l-1-5h-2l-1 5H6L5 11C3 9 2 5 4 3z" fill="none" stroke="#fff" stroke-width="1.3"/></defs></svg>
  <div class="abs" style="left:660px;top:187px;display:grid;grid-template-columns:232px 232px;column-gap:22px;row-gap:12px">
    <div class="svc-item active"><span class="svc-icon"><svg width="20" height="20" viewBox="0 0 20 20"><use href="#tooth"/></svg></span>Dental Implants</div>
    <div class="svc-item"><span class="svc-icon"><svg width="20" height="20" viewBox="0 0 20 20"><use href="#tooth"/></svg></span>Gum Disease</div>
    <div class="svc-item"><span class="svc-icon"><svg width="20" height="20" viewBox="0 0 20 20"><use href="#tooth"/></svg></span>Cosmetic Dentistry</div>
    <div class="svc-item"><span class="svc-icon"><svg width="20" height="20" viewBox="0 0 20 20"><use href="#tooth"/></svg></span>Root Canal</div>
    <div class="svc-item"><span class="svc-icon"><svg width="20" height="20" viewBox="0 0 20 20"><use href="#tooth"/></svg></span>Braces</div>
    <div class="svc-item"><span class="svc-icon"><svg width="20" height="20" viewBox="0 0 20 20"><use href="#tooth"/></svg></span>Dentures</div>
    <div class="svc-item"><span class="svc-icon"><svg width="20" height="20" viewBox="0 0 20 20"><use href="#tooth"/></svg></span>Crowns</div>
    <div class="svc-item"><span class="svc-icon"><svg width="20" height="20" viewBox="0 0 20 20"><use href="#tooth"/></svg></span>Emergency Dentistry</div>
    <div class="svc-item"><span class="svc-icon"><svg width="20" height="20" viewBox="0 0 20 20"><use href="#tooth"/></svg></span>Bridge</div>
    <div class="svc-item"><span class="svc-icon"><svg width="20" height="20" viewBox="0 0 20 20"><use href="#tooth"/></svg></span>Veneers</div>
    <div class="svc-item"><span class="svc-icon"><svg width="20" height="20" viewBox="0 0 20 20"><use href="#tooth"/></svg></span>&nbsp;&nbsp;Extractions</div>
    <div class="svc-item"><span class="svc-icon"><svg width="20" height="20" viewBox="0 0 20 20"><use href="#tooth"/></svg></span>&nbsp;&nbsp;ClearFit Aligners</div>
  </div>
</section>

<section class="reviews">
  <h2 class="abs center rv-title serif">What Our Patients Say About Us</h2>
  <p class="abs center rv-avg">Average Rating</p>
  <div class="abs rv-stars">
    <svg width="150" height="24" viewBox="0 0 150 24"><g fill="#f7c531"><path id="st" d="M12 1l3.3 7 7.7.9-5.7 5.2 1.5 7.6L12 17.9 5.2 21.7l1.5-7.6L1 8.9 8.7 8z"/><use href="#st" x="30"/><use href="#st" x="60"/><use href="#st" x="90"/><use href="#st" x="120"/></g></svg>
    <span class="rv-score">4.9</span>
  </div>
  <div class="abs rv-count">
    <svg width="34" height="34" viewBox="0 0 34 34"><circle cx="16" cy="15" r="13" fill="#00A9DD"/><path d="M8 25l-3 6 8-4z" fill="#00A9DD"/><circle cx="11" cy="15" r="1.8" fill="#fff"/><circle cx="16" cy="15" r="1.8" fill="#fff"/><circle cx="21" cy="15" r="1.8" fill="#fff"/></svg>
    <span>238 Reviews</span>
  </div>

  <svg class="abs chev" style="left:72px" width="16" height="30"><path d="M13 3L3 15l10 12" stroke="#00A9DD" fill="none" stroke-width="2"/></svg>
  <svg class="abs chev" style="left:1110px" width="16" height="30"><path d="M3 3l10 12L3 27" stroke="#00A9DD" fill="none" stroke-width="2"/></svg>

  <article class="abs rv-card" style="left:121px">
    <div class="rv-avatar" role="img" aria-label="Reviewer profile photo"></div>
    <div class="rv-name">Rhea D.</div>
    <div class="stars"><svg width="106" height="18" viewBox="0 0 150 24"><g fill="#f7c531"><use href="#st"/><use href="#st" x="30"/><use href="#st" x="60"/><use href="#st" x="90"/><use href="#st" x="120"/></g></svg></div>
    <p class="rv-body">I am so happy I found Bright Harbor in Harborview. This is a long over due review since I have been seeing them for almost two years. They are always so....</p>
    <div class="rv-date">05 October, 2021</div>
    <div class="rv-src">RateLine</div>
  </article>
  <article class="abs rv-card" style="left:447px">
    <div class="rv-avatar" role="img" aria-label="Reviewer profile photo"></div>
    <div class="rv-name">Marcus P.</div>
    <div class="stars"><svg width="106" height="18" viewBox="0 0 150 24"><g fill="#f7c531"><use href="#st"/><use href="#st" x="30"/><use href="#st" x="60"/><use href="#st" x="90"/><use href="#st" x="120"/></g></svg></div>
    <p class="rv-body">As most of us know going to the dentist isn't our favorite thing. But at this dental office the entire staff is super friendly, efficient, and professional. They actually ....</p>
    <div class="rv-date">05 October, 2021</div>
    <div class="rv-src">RateLine</div>
  </article>
  <article class="abs rv-card" style="left:773px">
    <div class="rv-avatar" role="img" aria-label="Reviewer profile photo"></div>
    <div class="rv-name">Lauren Y.</div>
    <div class="stars"><svg width="106" height="18" viewBox="0 0 150 24"><g fill="#f7c531"><use href="#st"/><use href="#st" x="30"/><use href="#st" x="60"/><use href="#st" x="90"/><use href="#st" x="120"/></g></svg></div>
    <p class="rv-body">Went here last July 2021 for the removal of my 1 impacted wisdom tooth. Office is clean, staff are courteous. Massage chair. Wait was quick. I chose the laughing...</p>
    <div class="rv-date">05 October, 2021</div>
    <div class="rv-src">RateLine</div>
  </article>
</section>

<section class="difference">
  <h2 class="abs diff-title serif">Experience the Bright<br>Harbor Difference</h2>
  <div class="abs diff-body">
    <p>Your smile is our #1 priority. At Bright Harbor, we provide affordable and expert dental solutions. Whether you are looking for a family dentist or have any emergency such as needing a root canal in Harborview, we are here for you! We want to keep your teeth healthy inside and out. We don't just clean teeth and send you on your way, we want to get to know you.</p>
    <p>We accept most HMO and PPO insurances. We offer various financing options through CarePay Plus, LendWell and In-House Plans.</p>
    <p>To constantly strive to achieve the highest level of skills and modern techniques and equipment so we can provide our patients with the best that Dentistry has to offer at our dental office in Harborview, Orange County, CA.</p>
    <p>We provide patients with the best experience you can find in all of Southern California. We provide a comfortable and friendly atmosphere to shatter any fears you may have. We supply you with all the information on your dental health options so you can feel comfortable in the choices you make, whether it's a routine check-up or dental implants in Harborview.</p>
  </div>
  <a class="abs diff-link">We are available for <span>Emergency</span> and Walk-ins.</a>
  <div class="abs diff-photo" role="img" aria-label="Patient smiling with open mouth during a dental mirror examination"></div>
</section>

<section class="cta">
  <h2 class="abs center cta-title serif">Committed to excellence in<br>Oral Health Care</h2>
  <p class="abs center cta-sub">Free Exam and X-Rays for New Patients</p>
  <a class="abs cta-btn serif">Book An Appointment</a>
</section>

<footer class="footer">
  <div class="abs f-brand">Bright Harbor</div>
  <a class="abs btn btn-teal f-btn">Book Your Free Appointment</a>

  <div class="abs f-head" style="left:338px">Contact Us</div>
  <div class="abs" style="left:336px;top:94px;width:240px">
    <div class="f-row"><svg width="16" height="20" viewBox="0 0 16 20"><path d="M8 1a6 6 0 00-6 6c0 5 6 12 6 12s6-7 6-12a6 6 0 00-6-6z" fill="#00BBA5"/><circle cx="8" cy="7" r="2.2" fill="#10222c"/></svg><span>248 East Marlow Ave., Suite B<br>Harborview, CA 92840</span></div>
    <div class="f-row" style="font-size:12.5px"><svg width="16" height="16" viewBox="0 0 16 16"><path d="M3 1l3 3-2 2c1 2 4 5 6 6l2-2 3 3-2 3C7 16 0 9 0 4z" fill="#00BBA5"/></svg><span>(714) 555-0182</span></div>
    <div class="f-row"><svg width="18" height="14" viewBox="0 0 18 14"><rect width="18" height="14" rx="2" fill="#00BBA5"/><path d="M1 2l8 6 8-6" stroke="#10222c" fill="none" stroke-width="1.4"/></svg><span>hello@mybrightharbor.com</span></div>
  </div>
  <div class="abs socials"><i></i><i></i><i></i><i></i></div>

  <div class="abs f-head" style="left:613px">Office Hours</div>
  <svg class="abs" style="left:612px;top:96px" width="18" height="18" viewBox="0 0 18 18"><circle cx="9" cy="9" r="7.5" stroke="#00BBA5" fill="none" stroke-width="1.6"/><path d="M9 5v4h3" stroke="#00BBA5" fill="none" stroke-width="1.6"/></svg>
  <div class="abs f-hours" style="left:644px;top:90px">Monday 10AM–7PM<br>Tuesday 10AM–7PM<br>Wednesday 9AM–6PM<br>Thursday 9AM–6PM<br>Friday 9AM–5PM<br>Saturday 9AM–1PM</div>

  <div class="abs f-head" style="left:888px">Location Map</div>
  <div class="abs map" role="img" aria-label="Street map showing the clinic location in Harborview"></div>
  <p class="abs f-links">Ridge Dental | Lakeside Dental | Bayfront Dental | Meadow Dental | Coastline Dental</p>
</footer>

<p class="abs center copy">©<span>Bright Harbor</span> - 2021 All rights reserved. &nbsp;| Disclaimer &amp; Terms | Privacy Policy | Sitemap</p>

</body>
</html>
```